New Website for Consulting Company

Our company needs a fresh web design to help us drive our business forward. We are a consulting and software provider to Airports, Air Traffic Organizations, Builders and Architects. We specialize in analyzing operations, monitoring noise levels and creating software to improve operations, meet customer requirements and improve public relations.
Additional Info:
- Additional requirements can be found in the Web Design Brief
- Logo and logo branding attached
Target Market(s)
Airlines, Airports, Government Agencies, and Real Estate Developers
Industry/Entity Type
Aviation
Coding
Coded - Design and coding required
Number of Pages Required
2 page
Colors
Designer to choose colors to be used in the design.
Requirements
Must have
- - Create a Wordpress Design (Coded - Design and coding required)
- - Designer must provide full implementation/coding depending on the platform chosen by the client (i.e. Wordpress theme, HTML/CSS, etc.)
- - This is a multi-page site; Supporting pages can be formatted the same, but links need to be in place
- - Colors used must be grey scale, black or match the logo. It is not necessary to use all the colors in our logo
Should not have
- We are not looking for an overly bright site. While our logo has 5 different colors, it is not necessary to use all of them.

```html
<!DOCTYPE html>
<html lang="en">
<head>
<meta charset="utf-8">
<title>SkyHarbor Consulting – Technical Consultants of Airports &amp; Air Traffic Organizations</title>
<link rel="stylesheet" href="https://fonts.googleapis.com/css2?family=Oswald:wght@300;400;500&family=Raleway:wght@400;500;600;700&display=swap">
<style>
:root{
  --blue:#2a72c0;
  --blue-dark:#0d4a8a;
  --blue-deep:#083a70;
  --topbar:#2f77c4;
  --ink:#333;
  --muted:#666;
  --light:#888;
  --line:#dcdcdc;
  --gray-band:#5e5e5e;
  --footer:#262626;
  --footer-bottom:#1d1d1d;
  --white:#fff;
}
*{margin:0;padding:0;box-sizing:border-box}
html,body{width:1200px;height:3358px;overflow:hidden}
body{font-family:"Raleway",sans-serif;color:var(--ink);background:var(--white);position:relative}
a{color:inherit;text-decoration:none}

.topbar{position:absolute;left:0;top:0;width:1200px;height:27px;background:linear-gradient(90deg,#f4f4f4 0 37%,var(--topbar) 37%)}
.topbar-info{position:absolute;right:60px;top:0;height:27px;display:flex;gap:60px;align-items:center;color:var(--white);font-size:12px}
.topbar-info span{display:flex;align-items:center;gap:8px}

.header{position:absolute;left:0;top:27px;width:1200px;height:103px;background:linear-gradient(#fff,#f2f2f2);border-bottom:1px solid var(--line)}
.brand{position:absolute;left:80px;top:30px;display:flex;align-items:center;gap:10px;font-family:"Raleway",sans-serif;font-weight:700;font-size:30px;color:var(--blue-dark)}
.brand-square{width:16px;height:16px;background:var(--blue)}
.nav{position:absolute;left:458px;top:0;display:flex;height:103px;align-items:center}
.nav a{font-family:"Oswald",sans-serif;font-size:13px;letter-spacing:.5px;color:var(--blue);padding:0 15px;height:103px;display:flex;align-items:center;border-right:1px solid #e3e3e3}
.nav a.active{color:var(--ink);border-top:3px solid var(--blue)}

.hero{position:absolute;left:0;top:130px;width:1200px;height:548px;background:linear-gradient(180deg,#7f9cc4 0%,#3f5f8e 35%,#2a3e5e 65%,#4b5a72 100%)}
.hero-title{position:absolute;left:0;top:230px;width:1200px;text-align:center;color:var(--white);font-family:"Oswald",sans-serif;text-transform:uppercase}
.hero-title .small{font-size:30px;font-weight:300;letter-spacing:2px}
.hero-title .big{font-size:42px;font-weight:400;color:#bfe0ff;letter-spacing:1px;margin-top:2px}

.categories{position:absolute;left:0;top:678px;width:1200px;height:694px}
.section-title{font-family:"Oswald",sans-serif;font-weight:400;text-transform:uppercase;text-align:center;color:#555;font-size:30px;letter-spacing:.5px}
.section-title::after{content:"";display:block;width:78px;height:2px;background:#999;margin:12px auto 0}
.categories .section-title{position:absolute;left:0;top:90px;width:1200px}
.categories-text{position:absolute;left:136px;top:192px;width:928px;text-align:center;font-size:13px;line-height:27px;color:var(--muted)}
.cat-list{position:absolute;left:100px;top:338px;width:1000px;display:flex;justify-content:space-between}
.cat{width:200px;text-align:center}
.cat-icon{width:116px;height:116px;border-radius:50%;border:2px solid var(--blue);margin:0 auto;display:flex;align-items:center;justify-content:center}
.cat.active .cat-icon{background:var(--blue)}
.cat-label{display:inline-block;margin-top:35px;font-size:15px;letter-spacing:1px;color:#444;padding:12px 20px;font-weight:500}
.cat.active .cat-label{background:#e2e2e2;color:var(--blue)}

.about{position:absolute;left:0;top:1372px;width:1200px;height:695px;background:linear-gradient(90deg,var(--blue-deep),var(--blue-dark) 50%,#0b4f93)}
.about h2{position:absolute;left:93px;top:112px;font-family:"Oswald",sans-serif;font-weight:400;font-size:30px;color:var(--white);text-transform:uppercase}
.about h2::after{content:"";display:block;width:160px;height:3px;background:var(--white);margin-top:16px}
.about-text{position:absolute;left:93px;top:222px;width:540px;color:#dfe9f5;font-size:12.5px;line-height:27px}
.about-text p+p{margin-top:20px}
.about-text b{color:var(--white)}
.btn{position:absolute;display:inline-block;border:2px solid var(--white);color:var(--white);font-family:"Oswald",sans-serif;font-size:16px;text-transform:uppercase;padding:6px 30px;letter-spacing:.5px}
.about .btn{left:93px;top:566px}
.about-photo{position:absolute;left:694px;top:66px;width:346px;height:629px;background:linear-gradient(180deg,#6f8fb0,#3e4c5e 60%,#2f3a48);border-radius:160px 160px 0 0}

.clients{position:absolute;left:0;top:2067px;width:1200px;height:602px}
.clients .section-title{position:absolute;left:0;top:102px;width:1200px}
.clients-sub{position:absolute;left:0;top:170px;width:1200px;text-align:center;font-size:13px;color:var(--muted)}
.arrows{position:absolute;right:60px;top:150px;display:flex;gap:20px}
.testimonials{position:absolute;left:78px;top:250px;width:1064px;display:flex;justify-content:space-between}
.testi{width:348px;border-left:1px solid var(--line);border-bottom:1px solid var(--line);padding:0 20px 30px 90px;position:relative;height:215px}
.quote{position:absolute;left:10px;top:14px;width:42px;height:42px;background:var(--blue);display:flex;align-items:center;justify-content:center}
.testi p{font-size:12.5px;line-height:22px;color:var(--muted)}
.testi .name{margin-top:10px;color:var(--blue);font-weight:700;font-size:13px}
.testi .role{font-style:italic;font-size:11.5px;color:var(--light)}

.showcase{position:absolute;left:0;top:2669px;width:1200px;height:358px;background:linear-gradient(180deg,#4a4a4a,#6d6d6d 55%,#8a8a8a)}
.showcase h3{position:absolute;top:30px;font-family:"Oswald",sans-serif;font-weight:400;font-size:30px;color:var(--white);text-transform:uppercase}
.showcase h3::after{content:"";display:block;width:160px;height:3px;background:var(--white);margin-top:10px}
.feature-media{position:absolute;left:118px;top:110px;width:372px;height:220px;background:linear-gradient(135deg,#0a2a6a,#1e58b8 55%,#0b2c68);border:6px solid #2c2c2c}
.product-text{position:absolute;left:626px;top:112px;width:270px;font-size:12.5px;line-height:22px;color:#eee}
.showcase .btn{left:636px;top:290px;font-size:15px;padding:5px 26px}
.product-name{position:absolute;left:920px;top:150px;font-family:"Raleway",sans-serif;font-weight:600;font-size:44px;color:#f2f2f2;letter-spacing:1px}

.footer{position:absolute;left:0;top:3027px;width:1200px;height:276px;background:var(--footer);color:#ccc}
.footer .brand{left:120px;top:96px;color:var(--white)}
.social{position:absolute;left:122px;top:164px;display:flex;gap:10px}
.social span{width:20px;height:20px;background:#555}
.fcol{position:absolute;top:48px}
.fcol h4{font-family:"Oswald",sans-serif;font-weight:400;font-size:14px;color:var(--white);text-transform:uppercase;margin-bottom:22px}
.fcol li{list-style:none;font-size:12px;line-height:27px;padding-left:22px;position:relative}
.fcol li::before{content:"";position:absolute;left:4px;top:11px;width:5px;height:5px;border-top:1px solid #888;border-right:1px solid #888;transform:rotate(45deg)}
.contact-row{display:flex;gap:14px;font-size:12px;line-height:22px;margin-bottom:12px}
.contact-row svg{flex:none;margin-top:4px}
.copyright{position:absolute;left:0;top:3303px;width:1200px;height:55px;background:var(--footer-bottom);color:#aaa;font-size:12px;text-align:center;line-height:55px}
</style>
</head>
<body>

<div class="topbar">
  <div class="topbar-info">
    <span><svg width="12" height="12" viewBox="0 0 24 24"><path fill="#fff" d="M6.6 10.8a15 15 0 006.6 6.6l2.2-2.2c.3-.3.7-.4 1-.2 1.1.4 2.3.6 3.6.6.6 0 1 .4 1 1V20c0 .6-.4 1-1 1A17 17 0 013 4c0-.6.4-1 1-1h3.5c.6 0 1 .4 1 1 0 1.3.2 2.5.6 3.6.1.3 0 .7-.2 1z"/></svg>+1 (555) 014-2200</span>
    <span><svg width="14" height="11" viewBox="0 0 24 18"><rect x="1" y="1" width="22" height="16" fill="none" stroke="#fff" stroke-width="2"/><path d="M1 1l11 9 11-9" fill="none" stroke="#fff" stroke-width="2"/></svg>info@skyharborconsult.com</span>
  </div>
</div>

<header class="header">
  <div class="brand"><span class="brand-square"></span>SkyHarbor</div>
  <nav class="nav">
    <a class="active" href="#">HOME</a>
    <a href="#">AIRPORTS</a>
    <a href="#">AIRSPACE</a>
    <a href="#">EMISSIONS</a>
    <a href="#">ACOUTICS</a>
    <a href="#">VISUALIZATION</a>
    <a href="#">ABOUT</a>
    <a href="#" style="border-right:0">CONTACT</a>
  </nav>
</header>

<section class="hero" role="img" aria-label="Photo of an airport terminal roadway with a plane flying overhead">
  <div class="hero-title">
    <div class="small">Technical Consultants of</div>
    <div class="big">Airports &amp; Air Traffic Organizations</div>
  </div>
</section>

<section class="categories">
  <h2 class="section-title">Categories of Operation</h2>
  <p class="categories-text">SkyHarbor Consulting invents and deploys innovative management and technology solutions that address complex noise and airspace issues for airports and residential communities. With more than two decades of experience and original software solutions, the company identifies problems precisely and solves them through a diagnostic process that mitigates political, community and technical concerns, and builds consensus for ideas and solutions.</p>
  <div class="cat-list">
    <div class="cat active">
      <div class="cat-icon"><svg width="60" height="60" viewBox="0 0 24 24"><path fill="#fff" d="M21 16v-2l-8-5V3.5a1.5 1.5 0 00-3 0V9l-8 5v2l8-2.5V19l-2 1.5V22l3.5-1 3.5 1v-1.5L13 19v-5.5z" transform="rotate(45 12 12)"/></svg></div>
      <div class="cat-label">AIRPORTS</div>
    </div>
    <div class="cat">
      <div class="cat-icon"><svg width="56" height="56" viewBox="0 0 24 24"><circle cx="12" cy="8" r="6" fill="none" stroke="#2a72c0" stroke-width="2"/><circle cx="12" cy="8" r="2" fill="#2a72c0"/><path d="M4 14l8 4 8-4v6l-8 3-8-3z" fill="#2a72c0"/></svg></div>
      <div class="cat-label">SOFTWARES</div>
    </div>
    <div class="cat">
      <div class="cat-icon"><svg width="60" height="60" viewBox="0 0 24 24"><path fill="#2a72c0" d="M3 9l14-6 2 1-7 4 6 1 1-1h2l-2 3-16 0z"/><rect x="4" y="14" width="5" height="8" fill="#2a72c0"/><rect x="10" y="12" width="5" height="10" fill="#2a72c0"/><rect x="16" y="15" width="4" height="7" fill="#2a72c0"/></svg></div>
      <div class="cat-label">NOISE &amp; EMISSIONS</div>
    </div>
    <div class="cat">
      <div class="cat-icon"><svg width="60" height="40" viewBox="0 0 24 16"><path d="M1 8c3-5 7-7 11-7s8 2 11 7c-3 5-7 7-11 7S4 13 1 8z" fill="none" stroke="#2a72c0" stroke-width="1.8"/><circle cx="12" cy="8" r="4" fill="#2a72c0"/></svg></div>
      <div class="cat-label">VISUALIZATION</div>
    </div>
  </div>
</section>

<section class="about">
  <h2>Who We Are</h2>
  <div class="about-text">
    <p><b>SkyHarbor Consulting</b> is known throughout the aviation industry as a company to turn to when in need of quality, trustworthy noise consulting. Our hard-won reputation over the past 25 years is based in action and is substantiated in our quality interaction with clients as well as the general public. We are proud of our team of airport and acoustic experts. In our organization, the principal members of the staff are not simply figure heads, but are personally involved with each client.</p>
    <p><b>SkyHarbor Consulting</b> provides consulting, support services, and airspace visualization for airports, government agencies and partners throughout the world. Our employees have been working in the field of acoustics and information systems for over 25 years; airports are the heart of our firm and continue to be our focus.</p>
  </div>
  <a class="btn" href="#">Know More</a>
  <div class="about-photo" role="img" aria-label="Photo of a smiling consultant in a grey suit offering a handshake"></div>
</section>

<section class="clients">
  <h2 class="section-title">What Our Clients Say?</h2>
  <p class="clients-sub">Read what our clients say about our level of service and the success that they have achieved.</p>
  <div class="arrows">
    <svg width="22" height="14" viewBox="0 0 22 14"><path d="M8 1L2 7l6 6M2 7h20" fill="none" stroke="#bbb" stroke-width="1.5"/></svg>
    <svg width="22" height="14" viewBox="0 0 22 14"><path d="M14 1l6 6-6 6M20 7H0" fill="none" stroke="#bbb" stroke-width="1.5"/></svg>
  </div>
  <div class="testimonials">
    <div class="testi">
      <div class="quote"><svg width="18" height="16" viewBox="0 0 18 16"><path fill="#fff" d="M0 16V8l4-8h3L5 7h3v9zm10 0V8l4-8h3l-2 7h3v9z"/></svg></div>
      <p>Lorem Ipsum is simply dummy text of the printing and typesetting industry. Lorem Ipsum has been the industry's standard dummy text ever since the 1500s, when an unknown printer took a galley of type and scrambled it to make a type specimen book.</p>
      <div class="name">Jhonathan D</div><div class="role">Director of Company</div>
    </div>
    <div class="testi">
      <div class="quote"><svg width="18" height="16" viewBox="0 0 18 16"><path fill="#fff" d="M0 16V8l4-8h3L5 7h3v9zm10 0V8l4-8h3l-2 7h3v9z"/></svg></div>
      <p>Lorem Ipsum is simply dummy text of the printing and typesetting industry. Lorem Ipsum has been the industry's standard dummy text ever since the 1500s, when an unknown printer took a galley of type and scrambled it to make a type specimen book.</p>
      <div class="name">Sharon</div><div class="role">Technical Manager of Company</div>
    </div>
    <div class="testi">
      <div class="quote"><svg width="18" height="16" viewBox="0 0 18 16"><path fill="#fff" d="M0 16V8l4-8h3L5 7h3v9zm10 0V8l4-8h3l-2 7h3v9z"/></svg></div>
      <p>Lorem Ipsum is simply dummy text of the printing and typesetting industry. Lorem Ipsum has been the industry's standard dummy text ever since the 1500s, when an unknown printer took a galley of type and scrambled it to make a type specimen book.</p>
      <div class="name">Jessica</div><div class="role">Asst. Manager of Company</div>
    </div>
  </div>
</section>

<section class="showcase">
  <h3 style="left:118px">Features</h3>
  <div class="feature-media" role="img" aria-label="Video gallery preview showing a blue flight-track map"></div>
  <h3 style="left:638px">AeroLens</h3>
  <p class="product-text">AEROLENS is a web-based application designed to create, evaluate and display flight operations in 3D. This software tool evaluates the acoustic and environmental impacts from new Performance Based Procedures as well as new runways and airfield configurations.</p>
  <a class="btn" href="#">View Details</a>
  <div class="product-name">AeroLens</div>
</section>

<footer class="footer">
  <div class="brand"><span class="brand-square"></span>SkyHarbor</div>
  <div class="social"><span></span><span></span><span></span><span></span><span></span></div>
  <div class="fcol" style="left:436px">
    <h4>Quick Links</h4>
    <ul><li>Home</li><li>About</li><li>Contact</li><li>Privacy Policy</li><li>Terms of Use</li></ul>
  </div>
  <div class="fcol" style="left:658px">
    <h4>Services</h4>
    <ul><li>Airports</li><li>Airspace</li><li>Emissions</li><li>Acoustics</li><li>Visualization</li></ul>
  </div>
  <div class="fcol" style="left:854px">
    <h4>Contact Info</h4>
    <div class="contact-row"><svg width="12" height="16" viewBox="0 0 12 16"><path fill="#aaa" d="M6 0a6 6 0 00-6 6c0 4.5 6 10 6 10s6-5.5 6-10a6 6 0 00-6-6zm0 8.5A2.5 2.5 0 116 3.5a2.5 2.5 0 010 5z"/></svg><div>SkyHarbor Consulting<br>1400 Harbor View Drive, Suite 300<br>Bayview, California 90000</div></div>
    <div class="contact-row"><svg width="14" height="14" viewBox="0 0 24 24"><path fill="#aaa" d="M6.6 10.8a15 15 0 006.6 6.6l2.2-2.2c.3-.3.7-.4 1-.2 1.1.4 2.3.6 3.6.6.6 0 1 .4 1 1V20c0 .6-.4 1-1 1A17 17 0 013 4c0-.6.4-1 1-1h3.5c.6 0 1 .4 1 1 0 1.3.2 2.5.6 3.6.1.3 0 .7-.2 1z"/></svg><div>+1 (555) 014-2200</div></div>
    <div class="contact-row"><svg width="14" height="14" viewBox="0 0 24 24"><rect x="3" y="2" width="18" height="20" fill="none" stroke="#aaa" stroke-width="2"/><path d="M7 7h10M7 12h10M7 17h6" stroke="#aaa" stroke-width="2"/></svg><div>+1 (555) 014-2205</div></div>
    <div class="contact-row"><svg width="14" height="11" viewBox="0 0 24 18"><rect x="1" y="1" width="22" height="16" fill="none" stroke="#aaa" stroke-width="2"/><path d="M1 1l11 9 11-9" fill="none" stroke="#aaa" stroke-width="2"/></svg><div>info@skyharborconsult.com</div></div>
  </div>
</footer>
<div class="copyright">©2010-17 SkyHarbor Consulting. All Rights Reserved.</div>

</body>
</html>
```